Step and Repeat Backdrop for wedding reception photo booth

Would like to have a Step and Repeat Backdrop (8 foot high by 10 foot wide) that incorporates the wedding logo (attached) and the names Elena and Gavin. Background should be white, and wedding colors are burgundy and gold. Show me creativity :-) I have included some random samples.

```html
<!DOCTYPE html>
<html lang="en">
<head>
<meta charset="utf-8">
<title>Elena &amp; Gavin – Step and Repeat Backdrop</title>
<link rel="stylesheet" href="https://fonts.googleapis.com/css2?family=Playfair+Display:wght@600&display=swap">
<style>
  :root {
    --page: #ffffff;
    --backdrop: #ffffff;
    --burgundy: #8b0a0f;
    --gold: #b8902f;
    --gold-light: #d2b05a;
    --gold-deep: #a77f22;
    --shadow: rgba(0, 0, 0, 0.28);
  }
  * { box-sizing: border-box; margin: 0; padding: 0; }
  html, body {
    width: 1200px;
    height: 600px;
    overflow: hidden;
    background: var(--page);
  }
  .canvas {
    position: relative;
    width: 1200px;
    height: 600px;
  }
  .backdrop {
    position: absolute;
    left: 250px;
    top: 20px;
    width: 700px;
    height: 560px;
    background: var(--backdrop);
    overflow: hidden;
    box-shadow: 8px 12px 22px var(--shadow);
    font-family: "Playfair Display", Georgia, serif;
    font-weight: 600;
    color: var(--gold);
  }
  .band {
    position: absolute;
    left: 0;
    width: 100%;
    height: 19px;
    background: var(--burgundy);
    z-index: 2;
  }
  .band--top { top: 0; }
  .band--bottom { bottom: 0; }

  .flourish {
    display: block;
    background: linear-gradient(180deg, var(--gold-light), var(--gold-deep));
    border-radius: 3px;
    opacity: 0.55;
  }

  .repeat-mark {
    position: absolute;
    width: 74px;
    height: 48px;
    transform: translate(-50%, -50%);
    display: flex;
    flex-direction: column;
    align-items: center;
    justify-content: space-between;
  }
  .repeat-mark .flourish {
    width: 58px;
    height: 11px;
  }
  .repeat-name {
    font-size: 10.5px;
    line-height: 1;
    white-space: nowrap;
  }

  .feature-mark {
    position: absolute;
    left: 353px;
    top: 282px;
    width: 270px;
    height: 274px;
    transform: translate(-50%, -50%);
    display: flex;
    flex-direction: column;
    align-items: center;
    justify-content: space-between;
  }
  .feature-mark .flourish {
    width: 264px;
    height: 80px;
  }
  .feature-name {
    font-size: 36px;
    font-weight: 600;
    line-height: 1;
    white-space: nowrap;
  }
</style>
</head>
<body>
<main class="canvas">
  <section class="backdrop" aria-label="Elena and Gavin step and repeat backdrop">
    <div class="band band--top"></div>

    <div class="repeat-mark" style="left:37px;top:105px"><span class="flourish" role="img" aria-label="Small gold scroll flourish"></span><span class="repeat-name">Elena &amp; Gavin</span><span class="flourish" role="img" aria-label="Small gold scroll flourish"></span></div>
    <div class="repeat-mark" style="left:37px;top:222px"><span class="flourish" role="img" aria-label="Small gold scroll flourish"></span><span class="repeat-name">Elena &amp; Gavin</span><span class="flourish" role="img" aria-label="Small gold scroll flourish"></span></div>
    <div class="repeat-mark" style="left:37px;top:340px"><span class="flourish" role="img" aria-label="Small gold scroll flourish"></span><span class="repeat-name">Elena &amp; Gavin</span><span class="flourish" role="img" aria-label="Small gold scroll flourish"></span></div>
    <div class="repeat-mark" style="left:37px;top:458px"><span class="flourish" role="img" aria-label="Small gold scroll flourish"></span><span class="repeat-name">Elena &amp; Gavin</span><span class="flourish" role="img" aria-label="Small gold scroll flourish"></span></div>

    <div class="repeat-mark" style="left:142px;top:46px"><span class="flourish" role="img" aria-label="Small gold scroll flourish"></span><span class="repeat-name">Elena &amp; Gavin</span><span class="flourish" role="img" aria-label="Small gold scroll flourish"></span></div>
    <div class="repeat-mark" style="left:142px;top:164px"><span class="flourish" role="img" aria-label="Small gold scroll flourish"></span><span class="repeat-name">Elena &amp; Gavin</span><span class="flourish" role="img" aria-label="Small gold scroll flourish"></span></div>
    <div class="repeat-mark" style="left:142px;top:282px"><span class="flourish" role="img" aria-label="Small gold scroll flourish"></span><span class="repeat-name">Elena &amp; Gavin</span><span class="flourish" role="img" aria-label="Small gold scroll flourish"></span></div>
    <div class="repeat-mark" style="left:142px;top:400px"><span class="flourish" role="img" aria-label="Small gold scroll flourish"></span><span class="repeat-name">Elena &amp; Gavin</span><span class="flourish" role="img" aria-label="Small gold scroll flourish"></span></div>
    <div class="repeat-mark" style="left:142px;top:514px"><span class="flourish" role="img" aria-label="Small gold scroll flourish"></span><span class="repeat-name">Elena &amp; Gavin</span><span class="flourish" role="img" aria-label="Small gold scroll flourish"></span></div>

    <div class="repeat-mark" style="left:248px;top:105px"><span class="flourish" role="img" aria-label="Small gold scroll flourish"></span><span class="repeat-name">Elena &amp; Gavin</span><span class="flourish" role="img" aria-label="Small gold scroll flourish"></span></div>
    <div class="repeat-mark" style="left:248px;top:458px"><span class="flourish" role="img" aria-label="Small gold scroll flourish"></span><span class="repeat-name">Elena &amp; Gavin</span><span class="flourish" role="img" aria-label="Small gold scroll flourish"></span></div>

    <div class="repeat-mark" style="left:353px;top:46px"><span class="flourish" role="img" aria-label="Small gold scroll flourish"></span><span class="repeat-name">Elena &amp; Gavin</span><span class="flourish" role="img" aria-label="Small gold scroll flourish"></span></div>
    <div class="repeat-mark" style="left:353px;top:514px"><span class="flourish" role="img" aria-label="Small gold scroll flourish"></span><span class="repeat-name">Elena &amp; Gavin</span><span class="flourish" role="img" aria-label="Small gold scroll flourish"></span></div>

    <div class="repeat-mark" style="left:459px;top:105px"><span class="flourish" role="img" aria-label="Small gold scroll flourish"></span><span class="repeat-name">Elena &amp; Gavin</span><span class="flourish" role="img" aria-label="Small gold scroll flourish"></span></div>
    <div class="repeat-mark" style="left:459px;top:458px"><span class="flourish" role="img" aria-label="Small gold scroll flourish"></span><span class="repeat-name">Elena &amp; Gavin</span><span class="flourish" role="img" aria-label="Small gold scroll flourish"></span></div>

    <div class="repeat-mark" style="left:563px;top:46px"><span class="flourish" role="img" aria-label="Small gold scroll flourish"></span><span class="repeat-name">Elena &amp; Gavin</span><span class="flourish" role="img" aria-label="Small gold scroll flourish"></span></div>
    <div class="repeat-mark" style="left:563px;top:164px"><span class="flourish" role="img" aria-label="Small gold scroll flourish"></span><span class="repeat-name">Elena &amp; Gavin</span><span class="flourish" role="img" aria-label="Small gold scroll flourish"></span></div>
    <div class="repeat-mark" style="left:563px;top:282px"><span class="flourish" role="img" aria-label="Small gold scroll flourish"></span><span class="repeat-name">Elena &amp; Gavin</span><span class="flourish" role="img" aria-label="Small gold scroll flourish"></span></div>
    <div class="repeat-mark" style="left:563px;top:400px"><span class="flourish" role="img" aria-label="Small gold scroll flourish"></span><span class="repeat-name">Elena &amp; Gavin</span><span class="flourish" role="img" aria-label="Small gold scroll flourish"></span></div>
    <div class="repeat-mark" style="left:563px;top:514px"><span class="flourish" role="img" aria-label="Small gold scroll flourish"></span><span class="repeat-name">Elena &amp; Gavin</span><span class="flourish" role="img" aria-label="Small gold scroll flourish"></span></div>

    <div class="repeat-mark" style="left:662px;top:105px"><span class="flourish" role="img" aria-label="Small gold scroll flourish"></span><span class="repeat-name">Elena &amp; Gavin</span><span class="flourish" role="img" aria-label="Small gold scroll flourish"></span></div>
    <div class="repeat-mark" style="left:662px;top:222px"><span class="flourish" role="img" aria-label="Small gold scroll flourish"></span><span class="repeat-name">Elena &amp; Gavin</span><span class="flourish" role="img" aria-label="Small gold scroll flourish"></span></div>
    <div class="repeat-mark" style="left:662px;top:340px"><span class="flourish" role="img" aria-label="Small gold scroll flourish"></span><span class="repeat-name">Elena &amp; Gavin</span><span class="flourish" role="img" aria-label="Small gold scroll flourish"></span></div>
    <div class="repeat-mark" style="left:662px;top:458px"><span class="flourish" role="img" aria-label="Small gold scroll flourish"></span><span class="repeat-name">Elena &amp; Gavin</span><span class="flourish" role="img" aria-label="Small gold scroll flourish"></span></div>

    <div class="feature-mark">
      <span class="flourish" role="img" aria-label="Gold scroll flourish with fleur-de-lis crowning the couple's names"></span>
      <h1 class="feature-name">Elena &amp; Gavin</h1>
      <span class="flourish" role="img" aria-label="Gold scroll flourish with fleur-de-lis beneath the couple's names"></span>
    </div>

    <div class="band band--bottom"></div>
  </section>
</main>
</body>
</html>
```